New Human Resources Outsourcing company needs a brochure to explain services

I need a brochure that describes my business and the services we offer.

Everything we do is on my website as well. www.kelvornstaffing.com

Target Market(s)

Business Owners (Manufacturing, I.T. Financial Services)

Industry/Entity Type

Business

```html
<!DOCTYPE html>
<html lang="en">
<head>
<meta charset="UTF-8">
<title>Kelvorn Staffing – Service Levels</title>
<link href="https://fonts.googleapis.com/css2?family=Ubuntu:ital,wght@0,400;1,700&display=swap" rel="stylesheet">
<style>
  :root {
    --premier-bg: #5a3cf2;
    --premier-deep: #4426d6;
    --premier-tile: #7b62f4;
    --elite-bg: #f4f4f7;
    --elite-text: #77777e;
    --elite-head: #6b6b72;
    --elite-lilac: #c3b6f0;
    --elite-mint: #cdeedd;
    --elite-grey: #d4d4dc;
    --deluxe-bg: #3fd98d;
    --deluxe-teal: #2a9f95;
    --deluxe-light: #5fe3a2;
    --white: #ffffff;
  }
  * { margin: 0; padding: 0; box-sizing: border-box; }
  html, body { width: 1200px; height: 848px; overflow: hidden; background: var(--white); }
  .brochure {
    position: relative;
    width: 1200px;
    height: 848px;
    display: flex;
    font-family: "Ubuntu", sans-serif;
  }
  .tier {
    position: relative;
    width: 400px;
    height: 848px;
    overflow: hidden;
  }
  .tier--premier { background: var(--premier-bg); color: var(--white); }
  .tier--elite { background: var(--elite-bg); color: var(--elite-text); }
  .tier--deluxe { background: var(--deluxe-bg); color: var(--white); }

  .tier__photo {
    position: absolute;
    left: 0; top: 0;
    width: 400px;
    height: 350px;
  }
  .tier--premier .tier__photo {
    background:
      radial-gradient(ellipse 120px 140px at 60px 110px, rgba(60,70,90,0.85), transparent 70%),
      radial-gradient(ellipse 110px 150px at 165px 120px, rgba(120,140,170,0.9), transparent 70%),
      radial-gradient(ellipse 90px 140px at 345px 190px, rgba(225,210,190,0.9), transparent 70%),
      linear-gradient(180deg, #e6ebf0 0%, #cfd6de 45%, #9aa6b4 100%);
    clip-path: polygon(0 0, 100% 0, 100% 99%, 0 81%);
  }
  .tier--elite .tier__photo {
    background:
      radial-gradient(circle 70px at 175px 120px, rgba(210,215,225,0.75), transparent 75%),
      radial-gradient(ellipse 160px 180px at 220px 140px, #5d6674, transparent 80%),
      linear-gradient(180deg, #3c434d 0%, #59616d 55%, #7d8590 100%);
    clip-path: polygon(0 0, 100% 0, 100% 81%, 50% 99%, 0 81%);
  }
  .tier--deluxe .tier__photo {
    background:
      radial-gradient(ellipse 120px 70px at 140px 150px, rgba(236,200,180,0.95), transparent 75%),
      radial-gradient(ellipse 140px 60px at 330px 150px, rgba(40,42,48,0.9), transparent 75%),
      linear-gradient(180deg, #c8cde8 0%, #b9bfdf 30%, #d9b993 48%, #c39c6f 100%);
    clip-path: polygon(0 0, 100% 0, 100% 78%, 0 97%);
  }

  .tier__pattern {
    position: absolute;
    left: 0; bottom: 0;
    width: 400px;
  }
  .tier--premier .tier__pattern {
    height: 300px;
    background:
      radial-gradient(ellipse 220px 120px at 200px 230px, var(--premier-tile), transparent 75%),
      linear-gradient(180deg, var(--premier-bg) 0%, var(--premier-deep) 100%);
  }
  .tier--elite .tier__pattern {
    height: 370px;
    background:
      radial-gradient(ellipse 140px 120px at 230px 260px, var(--elite-lilac), transparent 75%),
      radial-gradient(ellipse 160px 110px at 300px 110px, var(--elite-mint), transparent 75%),
      radial-gradient(ellipse 150px 150px at 80px 230px, var(--elite-grey), transparent 75%),
      linear-gradient(180deg, var(--elite-bg) 0%, #e6e4ee 100%);
  }
  .tier--deluxe .tier__pattern {
    height: 300px;
    background:
      radial-gradient(ellipse 150px 150px at 250px 230px, var(--deluxe-teal), transparent 75%),
      radial-gradient(ellipse 120px 100px at 360px 110px, var(--deluxe-light), transparent 75%),
      linear-gradient(180deg, var(--deluxe-bg) 0%, #38c18f 100%);
  }

  .tier__title {
    position: absolute;
    font-weight: 700;
    font-style: italic;
    font-size: 31px;
    line-height: 1;
  }
  .tier__text {
    position: absolute;
    font-size: 14px;
    line-height: 21.7px;
    font-weight: 400;
    white-space: nowrap;
  }
  .tier--premier .tier__title { left: 34px; top: 352px; }
  .tier--premier .tier__text { left: 35px; top: 391px; }
  .tier--elite .tier__title { left: 58px; top: 352px; color: var(--elite-head); }
  .tier--elite .tier__text { left: 58px; top: 391px; }
  .tier--deluxe .tier__title { left: 53px; top: 347px; }
  .tier--deluxe .tier__text { left: 53px; top: 387px; }
</style>
</head>
<body>
<main class="brochure">
  <section class="tier tier--premier">
    <div class="tier__photo" role="img" aria-label="Photo of business people smiling and shaking hands at a meeting table"></div>
    <div class="tier__pattern" role="img" aria-label="Decorative pattern of translucent purple cubes"></div>
    <h2 class="tier__title">Premier</h2>
    <p class="tier__text">This is our highest level of service providing your<br>company’s complete HR Department.<br>We will handle Benefit Administration, Employee<br>Relations and other HR functions. Your HR<br>professional will come on site two days per week<br>to handle all HR duties, meet with employees and<br>partner with Management on strategic planning<br>and organization development.</p>
  </section>

  <section class="tier tier--elite">
    <div class="tier__photo" role="img" aria-label="Photo of a businessman touching a hexagon interface with HR icons"></div>
    <div class="tier__pattern" role="img" aria-label="Decorative pattern of pale lilac, mint and grey cubes"></div>
    <h2 class="tier__title">Elite</h2>
    <p class="tier__text">With this level of service your HR<br>professional will come on site one day per<br>week to handle all HR duties with most<br>tasks being completed off-site. We will<br>provide you with the tools and off-site<br>support necessary to run an effective HR<br>Department.</p>
  </section>

  <section class="tier tier--deluxe">
    <div class="tier__photo" role="img" aria-label="Photo of hands using a computer mouse and keyboard on a wooden desk"></div>
    <div class="tier__pattern" role="img" aria-label="Decorative pattern of teal and green cubes"></div>
    <h2 class="tier__title">Deluxe</h2>
    <p class="tier__text">With this level of service your HR<br>professional will come on site once per<br>month and provide virtual HR support<br>with most tasks and support being<br>provided off-site. This level of service is<br>ideal for companies who do not require<br>an on-site presence and just need a back<br>office and trusted partner to ensure they<br>remain compliant.</p>
  </section>
</main>
</body>
</html>
```